CD-Cover-Design für Musikerin
Zielgruppe
Ich bin Musikerin und gebe Seminare. Zielgruppe sind alle die zu meinen Konzerten und Seminaren kommen.
Aufgabenstellung
künstlerisch und kreativ, verspielt

```html
<!DOCTYPE html>
<html lang="en">
<head>
<meta charset="utf-8">
<title>Lorina – CD Cover</title>
<link href="https://fonts.googleapis.com/css2?family=Carlito:wght@400;700&family=Dancing+Script:wght@700&display=swap" rel="stylesheet">
<style>
  :root {
    --magenta: #a3157c;
    --violet: #6c0a98;
    --orange: #ff6a13;
    --amber: #f7a31c;
    --gold: #c9a41a;
    --track: #9b12c9;
    --white: #ffffff;
    --paper: #ffffff;
  }
  * { margin: 0; padding: 0; box-sizing: border-box; }
  html, body { width: 1200px; height: 619px; overflow: hidden; background: var(--paper); }
  .canvas { position: relative; width: 1200px; height: 619px; font-family: "Carlito", sans-serif; }
  .panel {
    position: absolute; top: 21px; height: 576px;
    background: linear-gradient(90deg, var(--magenta) 0%, #8a0f8c 55%, var(--violet) 100%);
    overflow: hidden;
  }
  .panel--back { left: 23px; width: 575px; }
  .panel--front { left: 600px; width: 576px; }

  .intro {
    position: absolute; top: 22px; left: 0; width: 100%;
    text-align: center; color: var(--white); font-size: 13.4px; line-height: 15.2px;
  }
  .intro .signature { color: var(--gold); font-weight: 700; }

  .mandala {
    position: absolute; border-radius: 50%;
    background: radial-gradient(circle, var(--orange) 0%, #e8562a 55%, var(--amber) 72%, #e43d5f 100%);
  }
  .mandala--back { left: 105px; top: 72px; width: 380px; height: 380px; }
  .tracklist-disc {
    position: absolute; left: 197px; top: 164px; width: 196px; height: 196px;
    border-radius: 50%; background: var(--white);
  }
  .tracklist {
    position: absolute; left: 197px; top: 195px; width: 196px;
    list-style: none; text-align: center; font-weight: 700;
    font-size: 13px; line-height: 15.7px; color: var(--track);
  }
  .tracklist .num { color: var(--gold); }

  .contact {
    position: absolute; top: 454px; left: 0; width: 100%;
    text-align: center; color: var(--white); font-size: 11.4px; line-height: 14px;
  }
  .contact .links { color: var(--gold); font-weight: 700; }
  .credits {
    position: absolute; top: 492px; left: 0; width: 100%;
    text-align: center; color: var(--white); font-size: 12px; line-height: 13.5px;
  }

  .mandala--front { left: 68px; top: 38px; width: 458px; height: 458px; }
  .portrait {
    position: absolute; left: 119px; top: 89px; width: 356px; height: 356px; border-radius: 50%;
    border: 2px solid var(--gold);
    background: radial-gradient(circle at 50% 45%, #c98a6a 0%, #8a5a3a 40%, #2f5f2a 75%, #3d6a30 100%);
  }
  .title {
    position: absolute; left: 0; width: 100%; top: 340px;
    text-align: center; font-family: "Dancing Script", cursive; font-weight: 700;
    font-size: 190px; line-height: 1; color: var(--white);
    text-shadow: 4px 6px 6px rgba(60, 0, 60, 0.45);
    padding-left: 10px;
  }
</style>
</head>
<body>
<div class="canvas">
  <section class="panel panel--back">
    <p class="intro">
      Music is our means of transport and a direct communication with our essence. We would like<br>
      to take you there with our music. Communicating THIS is our joy. We thank you and enjoy…<br>
      Our music is inspired by the spirit of Oneness. <span class="signature">Lorina and Tavi</span>
    </p>

    <div class="mandala mandala--back" role="img" aria-label="Orange mandala ornament"></div>
    <div class="tracklist-disc"></div>
    <ol class="tracklist">
      <li><span class="num">1.</span> Suivre le vent</li>
      <li><span class="num">2.</span> Sa Re Ga Ma</li>
      <li><span class="num">3.</span> Blessings</li>
      <li><span class="num">4.</span> Stilles Vertrauen</li>
      <li><span class="num">5.</span> Shine</li>
      <li><span class="num">6.</span> Ananda</li>
      <li><span class="num">7.</span> Wir sind Licht</li>
      <li><span class="num">8.</span> Toward the Dawn</li>
    </ol>

    <p class="contact">
      Feel free to contact us. Booking, concerts and contact on our website:<br>
      <span class="links">http://www.LorinaandTavi.com / Mail: lorinavk@mailbox.org</span>
    </p>
    <p class="credits">
      All song written by Lorina Vesterholm-Kain.<br>
      All tracks performed by Lorina on vocals, guitar and harmonium and Tavi-Rong Lau on his celestial violin.<br>
      Special thanks to: Bruno Vell for his backing vocals on tracks 7 &amp; 8 and his sarot/sisa performance on track 8.<br>
      Jonas Fehrling playing the guitar on tracks 4 &amp; 7. / Marco Sunda playing the cajon on tracks 1 &amp; 3.<br>
      Luc Ferrand @ Quintone Studios for recording and mixdown SONA all rights reserved Lorina Vesterholm-Kain
    </p>
  </section>

  <section class="panel panel--front">
    <div class="mandala mandala--front" role="img" aria-label="Orange mandala ring framing the portrait"></div>
    <div class="portrait" role="img" aria-label="Portrait photo of the singer framed by ivy leaves"></div>
    <h1 class="title">Lorina</h1>
  </section>
</div>
</body>
</html>
```